Other Setting Screens

Let's start with the new design of the rest of the pages of the app... All this pages are simple but let's keep the same type of design. You can find all this pages on the settings portion of the app. -My Posts-My Favorites-Premium Account-Edit Profile-Change Password-Leave Feedback

Colors
3176b5
0255a3
ffffff

```html
<!DOCTYPE html>
<html lang="en">
<head>
<meta charset="utf-8">
<title>Settings Screens</title>
<link rel="stylesheet" href="https://fonts.googleapis.com/css2?family=Roboto:wght@300;400;500;700&display=swap">
<style>
:root{
  --bg:#e6eaed;
  --screen:#f8f9fa;
  --ink:#5b5f66;
  --ink-soft:#9aa0a6;
  --line:#c9cdd1;
  --cyan:#22b5e6;
  --brand:#3176b5;
  --navy:#0255a3;
  --deep:#2d3a8c;
  --alert:#e8194f;
  --star:#f5a623;
  --white:#ffffff;
  --pale:#eef5fb;
}
*{box-sizing:border-box;margin:0;padding:0}
html,body{width:1158px;height:1200px;overflow:hidden}
body{background:var(--bg);font-family:'Roboto',sans-serif;color:var(--ink)}
.board{display:grid;grid-template-columns:280px 280px;grid-template-rows:560px 560px;gap:30px 40px;justify-content:center;padding-top:25px}
.screen{position:relative;background:var(--screen);border-radius:36px;box-shadow:0 14px 34px rgba(40,60,90,.16);overflow:hidden}
.topbar{display:flex;align-items:center;height:58px;padding:0 20px}
.topbar .title{flex:1;text-align:center;font-size:13px;color:var(--ink);padding-right:14px}
.back{width:14px;height:14px}
.nav{position:absolute;left:0;right:0;bottom:0;height:58px;display:flex;align-items:center;justify-content:space-around;padding:0 6px;background:var(--screen)}
.nav-item{display:flex;flex-direction:column;align-items:center;gap:3px;font-size:7px;text-transform:uppercase;color:var(--ink);width:50px}
.nav-item svg{width:16px;height:16px}
.nav-item.active{color:var(--cyan)}
.nav-center{width:44px;height:44px;border-radius:50%;background:var(--white);box-shadow:0 4px 12px rgba(40,60,90,.18);display:flex;align-items:center;justify-content:center;margin-top:-18px;font-size:9px;font-weight:700;color:var(--brand)}
.btn{display:inline-flex;align-items:center;justify-content:center;border-radius:24px;color:var(--white);font-size:11px;text-transform:uppercase;letter-spacing:.3px;background:linear-gradient(90deg,var(--cyan),var(--deep));box-shadow:0 8px 16px rgba(45,58,140,.3);height:40px;padding:0 26px}
.btn.plain{text-transform:none;font-size:12px}
/* change password */
.pw-body{padding:6px 26px}
.pw-intro{font-size:13px;line-height:1.35;color:var(--ink);margin-bottom:26px}
.field{margin-bottom:26px}
.field label{display:block;font-size:11px;color:var(--ink);margin-bottom:22px}
.field .rule{height:1px;background:var(--line)}
.field .error{font-size:9px;color:var(--alert);text-align:right;margin-top:5px}
.pw-action{text-align:center;margin-top:10px}
/* membership */
.plans{padding:4px 18px;position:relative}
.plan{border-radius:22px;padding:20px 22px 36px;position:relative}
.plan.annual{background:var(--cyan);color:var(--white);margin-bottom:38px}
.plan.monthly{background:var(--pale);color:var(--deep)}
.plan .name{font-size:26px;font-weight:300}
.plan .kind{font-size:10px;font-weight:500}
.plan .price{font-size:34px;font-weight:300;margin-top:12px}
.plan .price sup{font-size:14px;font-weight:500}
.plan .price small{font-size:11px;font-weight:500}
.plan .btn{position:absolute;left:50%;bottom:-20px;transform:translateX(-50%);white-space:nowrap}
.plan.monthly .price{color:var(--navy)}
/* favourites */
.fav-list{padding:0 16px;display:flex;flex-direction:column;gap:12px}
.fav-card{background:var(--white);border-radius:16px;box-shadow:0 6px 16px rgba(40,60,90,.08);padding:12px 14px;display:grid;grid-template-columns:1fr 1fr;gap:4px 8px;position:relative}
.author{display:flex;align-items:center;gap:7px;grid-column:1/3}
.avatar{width:22px;height:22px;border-radius:50%;background:linear-gradient(135deg,#8c8f95,#4d5056)}
.author b{display:block;font-size:10px;font-weight:700;color:var(--ink)}
.author span{font-size:8px;color:var(--ink-soft)}
.partner{display:flex;align-items:center;gap:5px;font-size:17px;font-weight:500;color:var(--brand)}
.partner i{width:12px;height:12px;border-radius:50%;background:var(--cyan);display:block}
.partner.violet{color:#5b3fa6}
.partner.violet i{background:#5b3fa6}
.offer b{display:block;font-size:9px;font-weight:700;color:var(--ink)}
.stars{color:var(--star);font-size:11px;letter-spacing:1px}
.stars em{font-style:normal;color:var(--ink);font-size:9px;margin-left:4px}
.offer span{display:block;font-size:7px;color:var(--ink-soft)}
.more{position:absolute;right:12px;bottom:10px;font-size:10px;color:var(--brand);letter-spacing:1px;line-height:0}
/* profile */
.status{display:flex;justify-content:space-between;padding:12px 20px 0;font-size:8px;color:var(--ink)}
.profile-top{display:flex;justify-content:flex-end;padding:14px 20px 6px}
.profile-body{padding:0 22px}
.row{border-bottom:1px solid #e2e5e8;padding:7px 0;font-size:11px}
.row .k{font-size:9px;font-weight:500;color:var(--ink)}
.row .v{margin-top:3px;color:var(--ink)}
.row.toggle{display:flex;justify-content:space-between;align-items:center;border:0}
.switch{width:30px;height:16px;border-radius:8px;background:#dfe3e7;position:relative}
.switch::after{content:"";position:absolute;top:2px;left:16px;width:12px;height:12px;border-radius:50%;background:var(--white);box-shadow:0 1px 3px rgba(0,0,0,.2)}
.switch.on{background:linear-gradient(90deg,var(--cyan),var(--deep))}
.switch.on::after{left:2px}
.row .about{font-size:10px;line-height:1.4;margin-top:3px}
</style>
</head>
<body>
<main class="board">

  <!-- Change password -->
  <section class="screen">
    <header class="topbar">
      <svg class="back" viewBox="0 0 14 14"><path d="M9 2 4 7l5 5" fill="none" stroke="#3176b5" stroke-width="1.5"/></svg>
      <h1 class="title" style="font-weight:400">Change Password</h1>
    </header>
    <div class="pw-body">
      <p class="pw-intro">Enter your new password below, we are just been extra security</p>
      <div class="field"><label>Current Password</label><div class="rule"></div></div>
      <div class="field"><label>New Password</label><div class="rule"></div></div>
      <div class="field"><label>Confirm Password</label><div class="rule"></div><p class="error">Password not match</p></div>
      <div class="pw-action"><span class="btn plain">Change Password</span></div>
    </div>
    <nav class="nav">
      <span class="nav-item active"><svg viewBox="0 0 16 16"><path d="M2 8 8 3l6 5v6H2z" fill="none" stroke="currentColor" stroke-width="1.3"/></svg>Home</span>
      <span class="nav-item"><svg viewBox="0 0 16 16"><path d="M2 3h12v8H7l-3 3v-3H2z" fill="none" stroke="currentColor" stroke-width="1.3"/></svg>Messages</span>
      <span class="nav-center">Lumo</span>
      <span class="nav-item"><svg viewBox="0 0 16 16"><path d="M4 11V7a4 4 0 0 1 8 0v4l1 1H3z M7 14h2" fill="none" stroke="currentColor" stroke-width="1.3"/><circle cx="12.5" cy="4" r="2" fill="#e8194f"/></svg>Notification</span>
      <span class="nav-item"><svg viewBox="0 0 16 16"><circle cx="8" cy="5.5" r="3" fill="none" stroke="currentColor" stroke-width="1.3"/><path d="M2.5 14a5.5 5.5 0 0 1 11 0" fill="none" stroke="currentColor" stroke-width="1.3"/></svg>Profile</span>
    </nav>
  </section>

  <!-- Upgrade membership -->
  <section class="screen">
    <header class="topbar">
      <svg class="back" viewBox="0 0 14 14"><path d="M9 2 4 7l5 5" fill="none" stroke="#3176b5" stroke-width="1.5"/></svg>
      <h1 class="title" style="font-weight:400">Upgrade Membership</h1>
    </header>
    <div class="plans">
      <article class="plan annual">
        <p class="name">Premium</p>
        <p class="kind">Annual Membership</p>
        <p class="price"><sup>$</sup>19.99<small>/Yearly</small></p>
        <span class="btn">Upgrade Now</span>
      </article>
      <article class="plan monthly">
        <p class="name">Premium</p>
        <p class="kind">Monthly Membership</p>
        <p class="price"><sup>$</sup>1.99<small>/Monthly</small></p>
        <span class="btn">Upgrade Now</span>
      </article>
    </div>
    <nav class="nav">
      <span class="nav-item active"><svg viewBox="0 0 16 16"><path d="M2 8 8 3l6 5v6H2z" fill="none" stroke="currentColor" stroke-width="1.3"/></svg>Home</span>
      <span class="nav-item"><svg viewBox="0 0 16 16"><path d="M2 3h12v8H7l-3 3v-3H2z" fill="none" stroke="currentColor" stroke-width="1.3"/></svg>Messages</span>
      <span class="nav-center">Lumo</span>
      <span class="nav-item"><svg viewBox="0 0 16 16"><path d="M4 11V7a4 4 0 0 1 8 0v4l1 1H3z M7 14h2" fill="none" stroke="currentColor" stroke-width="1.3"/><circle cx="12.5" cy="4" r="2" fill="#e8194f"/></svg>Notification</span>
      <span class="nav-item"><svg viewBox="0 0 16 16"><circle cx="8" cy="5.5" r="3" fill="none" stroke="currentColor" stroke-width="1.3"/><path d="M2.5 14a5.5 5.5 0 0 1 11 0" fill="none" stroke="currentColor" stroke-width="1.3"/></svg>Profile</span>
    </nav>
  </section>

  <!-- Favourites -->
  <section class="screen">
    <header class="topbar">
      <svg class="back" viewBox="0 0 14 14"><rect x="1" y="1" width="5" height="5" fill="#3176b5"/><rect x="8" y="1" width="5" height="2" fill="#22b5e6"/><rect x="8" y="4" width="5" height="2" fill="#22b5e6"/><rect x="1" y="8" width="5" height="5" fill="#22b5e6"/><rect x="8" y="8" width="5" height="5" fill="#3176b5"/></svg>
      <h1 class="title" style="font-weight:400">Favourites</h1>
      <svg class="back" viewBox="0 0 14 14"><circle cx="7" cy="5" r="3.5" fill="none" stroke="#3176b5" stroke-width="1.5"/><path d="M7 8.5V13" stroke="#3176b5" stroke-width="1.5"/></svg>
    </header>
    <div class="fav-list">
      <article class="fav-card">
        <div class="author"><span class="avatar" role="img" aria-label="Profile photo of Marco Reyes"></span><div><b>Marco Reyes</b><span>2 hours ago</span></div></div>
        <div class="partner"><i></i>Nuvo</div>
        <div class="offer"><b>$50 Statement Credit</b><div class="stars">★★★★☆<em>4.5</em></div><span>$50 off on first order</span></div>
        <span class="more">•••</span>
      </article>
      <article class="fav-card">
        <div class="author"><span class="avatar" role="img" aria-label="Profile photo of Marco Reyes"></span><div><b>Marco Reyes</b><span>2 hours ago</span></div></div>
        <div class="partner violet"><i></i>Skylane</div>
        <div class="offer"><b>$50 Statement Credit</b><div class="stars">★★★★☆<em>4.5</em></div><span>$50 off on first order</span></div>
        <span class="more">•••</span>
      </article>
      <article class="fav-card">
        <div class="author"><span class="avatar" role="img" aria-label="Profile photo of Marco Reyes"></span><div><b>Marco Reyes</b><span>2 hours ago</span></div></div>
        <div class="partner violet"><i></i>Skylane</div>
        <div class="offer"><b>$50 Statement Credit</b><div class="stars">★★★★☆<em>4.5</em></div><span>$50 off on first order</span></div>
        <span class="more">•••</span>
      </article>
    </div>
    <nav class="nav">
      <span class="nav-item active"><svg viewBox="0 0 16 16"><path d="M2 8 8 3l6 5v6H2z" fill="none" stroke="currentColor" stroke-width="1.3"/></svg>Home</span>
      <span class="nav-item"><svg viewBox="0 0 16 16"><path d="M2 3h12v8H7l-3 3v-3H2z" fill="none" stroke="currentColor" stroke-width="1.3"/></svg>Messages</span>
      <span class="nav-center">Lumo</span>
      <span class="nav-item"><svg viewBox="0 0 16 16"><path d="M4 11V7a4 4 0 0 1 8 0v4l1 1H3z M7 14h2" fill="none" stroke="currentColor" stroke-width="1.3"/><circle cx="12.5" cy="4" r="2" fill="#e8194f"/></svg>Notification</span>
      <span class="nav-item"><svg viewBox="0 0 16 16"><circle cx="8" cy="5.5" r="3" fill="none" stroke="currentColor" stroke-width="1.3"/><path d="M2.5 14a5.5 5.5 0 0 1 11 0" fill="none" stroke="currentColor" stroke-width="1.3"/></svg>Profile</span>
    </nav>
  </section>

  <!-- Edit profile -->
  <section class="screen">
    <div class="status"><span>●●●●● Carrier</span><span>9:41 AM</span><span>100%</span></div>
    <div class="profile-top"><span class="btn">Get Premium</span></div>
    <div class="profile-body">
      <div class="row"><p class="k">Name</p><p class="v">Hana Ortis</p></div>
      <div class="row"><p class="k">City</p><p class="v">Harbourton, United Kingdom</p></div>
      <div class="row"><p class="k">E-mail</p><p class="v">hana.ortis@mailbox.example</p></div>
      <div class="row toggle"><p class="k">Show followers</p><span class="switch"></span></div>
      <div class="row toggle"><p class="k">Notifications</p><span class="switch on"></span></div>
      <div class="row"><p class="k">About me</p><p class="about">My name is Hana and this is platform is awesome! Sharing this valuable services ...</p></div>
      <div class="row"><p class="k">Subcription Plan</p><p class="v">Silver Plan</p></div>
    </div>
    <nav class="nav">
      <span class="nav-item active"><svg viewBox="0 0 16 16"><path d="M2 8 8 3l6 5v6H2z" fill="none" stroke="currentColor" stroke-width="1.3"/></svg>Home</span>
      <span class="nav-item"><svg viewBox="0 0 16 16"><path d="M2 3h12v8H7l-3 3v-3H2z" fill="none" stroke="currentColor" stroke-width="1.3"/></svg>Messages</span>
      <span class="nav-center">Lumo</span>
      <span class="nav-item"><svg viewBox="0 0 16 16"><path d="M4 11V7a4 4 0 0 1 8 0v4l1 1H3z M7 14h2" fill="none" stroke="currentColor" stroke-width="1.3"/><circle cx="12.5" cy="4" r="2" fill="#e8194f"/></svg>Notification</span>
      <span class="nav-item"><svg viewBox="0 0 16 16"><circle cx="8" cy="5.5" r="3" fill="none" stroke="currentColor" stroke-width="1.3"/><path d="M2.5 14a5.5 5.5 0 0 1 11 0" fill="none" stroke="currentColor" stroke-width="1.3"/></svg>Profile</span>
    </nav>
  </section>

</main>
</body>
</html>
```